Business Card Design

Tarni Netball Australia
Refer to the attached logo
Require a business card layout, 2 sides
Pls use:
Doyle Perkins
Operations Manager
PO Box 61, Marrowvale NSW 2561
admin@tarnina.com.au
0482 316 905

We love the black and white coloring with a possible splash of green and orange.

Industry/Entity Type

Business

Colors
f37122
9bcb3c

```html
<!DOCTYPE html>
<html lang="en">
<head>
<meta charset="utf-8">
<title>Doyle Perkins – Business Card</title>
<link rel="stylesheet" href="https://fonts.googleapis.com/css2?family=Arvo:wght@700&family=Tinos:wght@400;700&family=Arimo:wght@700&display=swap">
<style>
  :root {
    --page: #ffffff;
    --card: #0a0a0a;
    --ink: #ffffff;
    --lime: #9bcb3c;
    --flame: #f0341c;
    --orange: #f37122;
  }
  html, body {
    margin: 0;
    width: 1200px;
    height: 900px;
    overflow: hidden;
    background: var(--page);
  }
  .card {
    position: absolute;
    left: 75px;
    top: 150px;
    width: 1050px;
    height: 600px;
    background: var(--card);
    overflow: hidden;
    color: var(--ink);
  }
  .splash {
    position: absolute;
  }
  .splash--lime {
    left: -60px;
    top: -60px;
    width: 360px;
    height: 420px;
    background: radial-gradient(ellipse at 20% 20%, rgba(155,203,60,0.95) 0%, rgba(155,203,60,0.45) 35%, rgba(155,203,60,0) 70%);
  }
  .splash--flame {
    right: -60px;
    bottom: -60px;
    width: 300px;
    height: 420px;
    background: radial-gradient(ellipse at 75% 60%, rgba(240,52,28,0.9) 0%, rgba(243,113,34,0.4) 38%, rgba(240,52,28,0) 70%);
  }
  .name {
    position: absolute;
    left: 0;
    width: 1040px;
    top: 116px;
    margin: 0;
    text-align: center;
    font-family: "Arvo", Georgia, serif;
    font-weight: 700;
    font-size: 76px;
    letter-spacing: 1px;
    line-height: 1;
  }
  .role {
    position: absolute;
    left: 197px;
    top: 208px;
    width: 655px;
    display: flex;
    align-items: center;
    gap: 18px;
    font-family: "Tinos", "Times New Roman", serif;
    font-size: 37px;
    letter-spacing: 1.5px;
    line-height: 1;
  }
  .role::before, .role::after {
    content: "";
    flex: 1;
    height: 1px;
    background: var(--ink);
  }
  .phone {
    position: absolute;
    left: 0;
    width: 1050px;
    top: 366px;
    text-align: center;
    font-family: "Arimo", Arial, sans-serif;
    font-weight: 700;
    font-size: 90px;
    letter-spacing: 4px;
    line-height: 1;
  }
  .bullet {
    position: absolute;
    top: 390px;
    width: 38px;
    height: 38px;
  }
  .bullet--left { left: 134px; }
  .bullet--right { left: 875px; }
  .address {
    position: absolute;
    left: 0;
    width: 1050px;
    top: 472px;
    text-align: center;
    font-family: "Tinos", "Times New Roman", serif;
    font-size: 37px;
    letter-spacing: 1px;
    line-height: 1;
  }
  .email {
    position: absolute;
    left: 0;
    width: 1050px;
    top: 541px;
    text-align: center;
    font-family: "Tinos", "Times New Roman", serif;
    font-weight: 700;
    font-size: 38px;
    letter-spacing: 2px;
    line-height: 1;
  }
</style>
</head>
<body>
  <div class="card">
    <div class="splash splash--lime" role="img" aria-label="Green paint splatter"></div>
    <div class="splash splash--flame" role="img" aria-label="Red-orange paint splatter"></div>

    <h1 class="name">Doyle Perkins</h1>
    <div class="role">Operations Manager</div>

    <svg class="bullet bullet--left" viewBox="0 0 40 40" aria-hidden="true"><polygon points="20,3 38,16 31,37 9,37 2,16" fill="#ffffff"/></svg>
    <div class="phone">0482-316-905</div>
    <svg class="bullet bullet--right" viewBox="0 0 40 40" aria-hidden="true"><polygon points="20,3 38,16 31,37 9,37 2,16" fill="#ffffff"/></svg>

    <div class="address">PO Box 61, Marrowvale NSW 2561</div>
    <div class="email">admin@tarnina.com.au</div>
  </div>
</body>
</html>
```